Harlan Whitcombe Accounting Flyer

A one page flyer to promote our 2009 season taxation return price of $95.00 GST Inclusive. Some text items we do require on the flyer are as follows:

- Two office addresses & phone numbers - 21 King Street Scottsdale - 03 61847203 & 5/62 Tindall Road George Town - 03 61590836

  - Basic Individual taxation returns completed for just $95* - just mention this offer when booking an appointment or dropping off your information. We will lodge your return electronically for you as well - no extra charge!

Does not include supplemental work such as taxpayers with rental properties or supplementary schedule requirements which will incur extra fees.
Updates

Please make sure the firm''s name is included in the flyer and the words - taxation return - only is required not the year it is for ie: 2009.

The firm name and contacts need to be prominately displayed to ensure clients are drawn to the firm and can contact us easily.
The price is also an important feature as this is the main thing clients are interested in for this type of work.

Target Market(s)

General public who require Individual taxation returns.  

Industry/Entity Type

Accounting

Requirements
Must have
• Disclaimers as listed in the ''''describe what you want'''' box.
Nice to have
• Brightly coloured, professional modern feel about the graphics, surprise us!
Should not have
• Any animated characters.

```html
<!DOCTYPE html>
<html lang="en">
<head>
<meta charset="utf-8">
<title>Harlan Whitcombe Accounting – Taxation Returns</title>
<link rel="stylesheet" href="https://fonts.googleapis.com/css2?family=Dancing+Script:wght@500&family=Josefin+Sans:wght@600&family=Arimo:ital@0;1&display=swap">
<style>
  :root {
    --plum-light: #7a4a69;
    --plum-dark: #42283d;
    --gold: #e8ac32;
    --ink-plum: #4a2540;
    --white: #ffffff;
    --sky-top: #d4d4d4;
    --sky-haze: #e4e4e4;
    --horizon: #f2f2f2;
    --sea-mid: #8c8c8c;
    --sea-deep: #555555;
    --sail-shade: #7a7a7a;
  }
  * { margin: 0; padding: 0; box-sizing: border-box; }
  html, body { width: 927px; height: 1200px; overflow: hidden; background: var(--white); }
  .flyer { position: relative; width: 927px; height: 1200px; overflow: hidden; background: var(--plum-dark); }

  .hero {
    position: absolute; left: 0; top: 0; width: 927px; height: 600px;
    background:
      radial-gradient(ellipse 260px 300px at 250px 250px, rgba(90,90,90,0.55), rgba(90,90,90,0) 70%),
      radial-gradient(ellipse 120px 170px at 700px 300px, rgba(200,200,200,0.5), rgba(200,200,200,0) 70%),
      linear-gradient(180deg, var(--sky-top) 0%, var(--sky-haze) 40%, var(--horizon) 71%, #bdbdbd 73%, var(--sea-mid) 85%, var(--sea-deep) 100%);
  }
  .tagline { position: absolute; font-family: "Dancing Script", cursive; font-weight: 500; line-height: 1; white-space: nowrap; }
  .tagline--lead { left: 452px; top: 52px; font-size: 49px; color: var(--gold); }
  .tagline--follow { left: 589px; top: 112px; font-size: 43px; color: var(--ink-plum); }

  .locations {
    position: absolute; left: 0; top: 600px; width: 309px; height: 600px;
    background: var(--plum-light); color: var(--white); text-align: center;
    font-family: "Arimo", Arial, sans-serif;
  }
  .locations__title {
    margin-top: 108px; font-family: "Josefin Sans", sans-serif; font-weight: 600;
    font-size: 23px; letter-spacing: 2px; color: var(--gold); text-transform: uppercase;
  }
  .office { font-size: 17.5px; line-height: 24.5px; }
  .office--first { margin-top: 46px; }
  .office--second { margin-top: 48px; }

  .offer {
    position: absolute; left: 309px; top: 600px; width: 618px; height: 600px;
    padding-left: 18px; text-align: center; color: var(--white);
  }
  .offer__headline {
    margin: 54px auto 0; width: 520px;
    font-family: "Josefin Sans", sans-serif; font-weight: 600;
    font-size: 34px; line-height: 46px; letter-spacing: 2.5px; text-transform: uppercase;
  }
  .offer__body {
    margin: 56px auto 0; width: 520px;
    font-family: "Arimo", Arial, sans-serif; font-size: 20px; line-height: 27.6px;
  }
  .offer__note {
    margin: 20px auto 0; width: 520px;
    font-family: "Arimo", Arial, sans-serif; font-style: italic; font-size: 11.5px; line-height: 18px;
  }

  .swoosh { position: absolute; left: 0; top: 1040px; width: 927px; height: 80px; }

  .firm-name {
    position: absolute; left: 0; top: 1124px; width: 880px; text-align: center;
    font-family: "Dancing Script", cursive; font-weight: 500; font-size: 35px; color: var(--white);
  }
</style>
</head>
<body>
<main class="flyer">
  <div class="hero" role="img" aria-label="Black and white photograph of two racing yachts under full sail on sparkling open water"></div>
  <p class="tagline tagline--lead">Sail smoothly</p>
  <p class="tagline tagline--follow">through tax season</p>

  <section class="locations">
    <h2 class="locations__title">Locations</h2>
    <p class="office office--first">21 King Street<br>Scottsdale<br>P: 03 61847203</p>
    <p class="office office--second">5/62 Tindall Road<br>George Town<br>P: 03 61590836</p>
  </section>

  <section class="offer">
    <h1 class="offer__headline">Taxation returns for<br>only $95!*</h1>
    <p class="offer__body">Basic Individual Taxation Returns<br>completed for just $95.* Just mention this offer<br>when booking an appointment or dropping off<br>your information. We will lodge your return<br>electronically for you as well.<br>No extra charge!</p>
    <p class="offer__note">*Does not include supplemental work such as taxpayers with rental properties or<br>supplementary schedule requirements which will incur extra fees.</p>
  </section>

  <svg class="swoosh" viewBox="0 0 927 80" aria-hidden="true">
    <path d="M0 38 C250 14 650 10 927 28" fill="none" stroke="#e8ac32" stroke-width="1"/>
    <path d="M0 46 C260 22 640 18 927 36" fill="none" stroke="#c9567a" stroke-width="1"/>
    <path d="M0 52 C280 30 620 30 927 44" fill="none" stroke="#ffffff" stroke-width="1.2" opacity="0.9"/>
    <path d="M0 58 C300 38 600 40 927 50" fill="none" stroke="#ffffff" stroke-width="0.8" opacity="0.7"/>
    <path d="M0 64 C320 46 600 50 927 58" fill="none" stroke="#d8b8cc" stroke-width="0.8" opacity="0.6"/>
  </svg>

  <p class="firm-name">Harlan Whitcombe Accounting</p>
</main>
</body>
</html>
```